Educational Institution needs a new website

A little bit about ourselves:
Brimley College is a multicultural K-12 school with students who represent nearly 30 ethnic and cultural backgrounds. It is one of the fastest growing schools in the City of Canning (in Perth, Western Australia), and offers quality education with a unique school environment at two campuses.
The mission of Brimley College is to equip students with moral values, academic knowledge and 21st century skills. We empower students to unlock their potential to be confident global citizens.
Brimley College strives to educate students in a manner which inspires them to become lifelong learners. We are committed to raising individuals who are tolerant and respectful towards others enabling them to grow into citizens who contribute to the common good of society.
Here are our design goals:
#1: To emphasise the growth of the school from a small school community to a much larger prestigious college.
#2: Have current and prospective parents have a clear understanding of our college’s morals and values and how we differ from other colleges.
#3: Highlight that our school provides a joyful and safe environment, which is highly valued by parents.
#4: Emphasise that our school presents a welcoming atmosphere for parents as we have strong relationships with our community.
#5: Highlight the various after-school activities available to our students, which are provided through the clubs and pastoral care department.
#6: Allow for online registrations and the option of adding student, staff and parent portals.
#7: Follow the existing school colours
We would like to request the design for the home page and a secondary page to see the alternative layouts.
Other information:
Please note that our logo is will be changed slightly in the upcoming weeks. Please keep this in mind while designing.
We will have another contest for the coding of the website.
We want to be able to make amendments and additions to the content of the website in the future and would like to make sure we have a strong communication with the designer.
The existing website is https://www.brimley-example.edu.au/ for reference for school colours and content.
Education

```html
<!DOCTYPE html>
<html lang="en">
<head>
<meta charset="utf-8">
<title>Brimley College</title>
<link href="https://fonts.googleapis.com/css2?family=Montserrat:wght@400;500;600;700&display=swap" rel="stylesheet">
<style>
:root{
  --blue:#1565a3;
  --sky:#27a6df;
  --ink:#1f2a36;
  --white:#ffffff;
  --pale:#f4f5f6;
  --line:#d9dde2;
}
*{margin:0;padding:0;box-sizing:border-box}
html,body{width:696px;height:1200px;overflow:hidden}
body{position:relative;background:var(--white);font-family:"Montserrat",sans-serif;color:var(--ink)}
.abs{position:absolute}

/* header */
.brand{left:51px;top:18px;display:flex;align-items:center;gap:6px}
.brand-dot{width:22px;height:22px;border-radius:50%;background:var(--sky)}
.brand-name{font-weight:700;font-size:14px;color:var(--blue);letter-spacing:.3px;line-height:1}
.social{display:flex;gap:5px}
.social span{width:16px;height:16px;border-radius:50%;background:var(--blue);display:block}
.social span.on{background:var(--sky)}
.head-social{left:367px;top:12px}
.search{left:434px;top:10px;width:119px;height:20px;border:1px solid var(--line);border-radius:10px;font-size:8px;color:#666;padding:5px 9px}
.search i{position:absolute;right:2px;top:2px;width:15px;height:15px;border-radius:50%;background:var(--blue)}
.login{left:563px;top:10px;width:82px;height:20px;background:var(--blue);color:var(--white);font-size:8px;font-weight:600;text-align:center;line-height:20px;border-radius:2px}
.nav{left:216px;top:40px;display:flex;gap:16px;font-size:8.4px;font-weight:500}

/* hero */
.hero{left:0;top:60px;width:696px;height:282px;background:linear-gradient(120deg,#c9b9a4,#6b7a58 40%,#b6a08a 60%,#3d4f74);clip-path:polygon(0 0,100% 0,100% 228px,50% 281px,0 228px)}
.dots{left:326px;top:310px;display:flex;gap:7px}
.dots span{width:9px;height:9px;border:1.2px solid var(--white);border-radius:50%}
.dots span.on{background:var(--white);border-color:var(--blue);box-shadow:inset 0 0 0 2px var(--white),inset 0 0 0 5px var(--blue)}

/* campuses */
.campus-photo{top:396px;width:264px;height:151px}
.campus-box{top:430px;width:105px;height:84px;background:var(--blue);border-radius:3px;color:var(--white);text-align:center;font-weight:700;font-size:10.5px;line-height:14px;padding-top:18px}
.campus-btn{display:block;margin:12px auto 0;width:79px;height:19px;border-radius:3px;font-size:8px;font-weight:500;line-height:19px;background:#000}
.campus-btn.alt{background:var(--sky)}
.campus-btn svg{vertical-align:-1px;margin-right:3px}

/* announcements */
.news-band{left:0;top:595px;width:696px;height:295px;background:var(--blue)}
.news-title{left:0;top:636px;width:696px;text-align:center;color:var(--white);font-size:19px;font-weight:600;letter-spacing:.5px}
.news-photo{top:678px;width:184px;height:126px}
.news-card{top:779px;width:164px;height:64px;background:var(--white);padding:12px 14px}
.news-card h3{font-size:9.6px;font-weight:500;color:var(--blue);line-height:12px;height:28px}
.news-meta{font-size:6.8px;display:flex;gap:10px;margin-top:5px;align-items:center}
.news-meta b{display:inline-block;width:7px;height:7px;border:1px solid var(--blue);border-radius:1px;margin-right:3px;vertical-align:-1px}
.news-meta b.clock{border-radius:50%}
.drag{left:626px;top:743px;width:38px;height:38px;border-radius:50%;background:var(--white);text-align:center;font-size:5.5px;padding-top:10px}

/* quick links */
.quick{top:937px;width:100px;height:100px;border-radius:50%;background:var(--pale);box-shadow:0 0 0 2px var(--white),0 0 0 3px #e6e8ea;display:flex;flex-direction:column;align-items:center;justify-content:center;text-align:center;font-size:7.8px;font-weight:500;line-height:10px;gap:6px;color:var(--ink)}
.quick.on{background:var(--blue);color:var(--white)}

/* footer */
.ribbon{left:0;top:1084px;width:696px;height:94px;background:var(--blue);color:var(--white)}
.ribbon h4{position:absolute;left:51px;top:31px;font-size:9.5px;font-weight:700;letter-spacing:.3px}
.ribbon p{position:absolute;left:51px;top:52px;width:320px;font-size:6.9px;line-height:10.5px}
.ribbon p u{font-weight:500}
.stat{top:34px;text-align:center}
.stat small{display:block;font-size:6.5px}
.stat strong{display:block;font-size:10.5px;font-weight:700;margin-top:4px}
.divider{left:551px;top:32px;width:1px;height:34px;background:rgba(255,255,255,.35)}
.bottom{left:0;top:1178px;width:696px;height:22px;background:var(--sky);color:var(--white);font-size:7.3px;padding:6px 51px}
.foot-social{left:587px;top:1181px}
.top-btn{left:664px;top:1148px}
</style>
</head>
<body>

<header>
  <div class="abs brand"><span class="brand-dot"></span><span class="brand-name">BRIMLEY COLLEGE</span></div>
  <div class="abs social head-social" aria-label="Social links"><span></span><span></span><span class="on"></span></div>
  <div class="abs search">Search<i></i></div>
  <div class="abs login">LOGIN PORTAL</div>
  <nav class="abs nav"><span>About Us</span><span>Learning</span><span>Student Life</span><span>Enrolment</span><span>Commmunity</span><span>News &amp; Events</span><span>Contact Us</span></nav>
</header>

<section>
  <div class="abs hero" role="img" aria-label="Young students playing with coloured wooden blocks in a classroom"></div>
  <svg class="abs" style="left:0;top:300px" width="696" height="56" aria-hidden="true">
    <polygon points="129,10 348,44 565,10 348,51" fill="#27a6df"/>
  </svg>
  <div class="abs dots"><span></span><span class="on"></span><span></span></div>
</section>

<section>
  <div class="abs campus-photo" style="left:51px;background:linear-gradient(110deg,#6f9a52,#c79a5c 45%,#8c9aa4 80%,#a7c2de)" role="img" aria-label="Modern campus building with timber screens and gardens"></div>
  <div class="abs campus-box" style="left:230px">ASHGROVE<br>CAMPUS
    <span class="campus-btn"><svg width="6" height="8" viewBox="0 0 6 8"><path d="M3 .5a2.3 2.3 0 0 1 2.3 2.3C5.3 4.6 3 7.4 3 7.4S.7 4.6.7 2.8A2.3 2.3 0 0 1 3 .5z" fill="none" stroke="#fff" stroke-width=".8"/></svg>Live Location</span></div>
  <div class="abs campus-photo" style="left:361px;background:linear-gradient(180deg,#5aaee6,#a7cde8 45%,#6f9a4a 70%,#4a6a36)" role="img" aria-label="Campus clock tower beside sports fields"></div>
  <div class="abs campus-box" style="left:540px">ELMRIDGE<br>CAMPUS
    <span class="campus-btn alt"><svg width="6" height="8" viewBox="0 0 6 8"><path d="M3 .5a2.3 2.3 0 0 1 2.3 2.3C5.3 4.6 3 7.4 3 7.4S.7 4.6.7 2.8A2.3 2.3 0 0 1 3 .5z" fill="none" stroke="#fff" stroke-width=".8"/></svg>Live Location</span></div>
</section>

<section>
  <div class="abs news-band"></div>
  <h2 class="abs news-title">ANNOUNCEMENTS</h2>

  <div class="abs news-photo" style="left:51px;background:linear-gradient(135deg,#8fb7c4,#e6e6e6 40%,#9a9ea4)" role="img" aria-label="Club open day event poster"></div>
  <div class="abs news-card" style="left:61px"><h3>Connecting with our community</h3>
    <div class="news-meta"><span><b></b>Nov 30, 2022</span><span><b class="clock"></b>3:15 PM to 4:30 PM</span></div></div>

  <div class="abs news-photo" style="left:256px;background:linear-gradient(135deg,#2e6870,#4d7f86 50%,#2a5a62)" role="img" aria-label="Collage of students at a science fair"></div>
  <div class="abs news-card" style="left:266px"><h3>where curiosity inspires solution steam fest</h3>
    <div class="news-meta"><span><b></b>Oct 22, 2022</span><span><b class="clock"></b>11 AM to 3 PM</span></div></div>

  <div class="abs news-photo" style="left:461px;background:linear-gradient(120deg,#6b4a3c,#b23a3a 50%,#d9c8bf)" role="img" aria-label="Students dressed up for a school event"></div>
  <div class="abs news-card" style="left:471px"><h3>Connecting with our community</h3>
    <div class="news-meta"><span><b></b>Nov 30, 2022</span><span><b class="clock"></b>3:15 PM to 4:30 PM</span></div></div>

  <div class="abs drag"><svg width="12" height="8" viewBox="0 0 12 8"><path d="M1 4h10M7.5 1 11 4 7.5 7" fill="none" stroke="#1f2a36" stroke-width="1"/></svg><br>DRAG</div>
</section>

<section>
  <div class="abs quick" style="left:111px">
    <svg width="28" height="26" viewBox="0 0 28 26"><rect x="1" y="2" width="26" height="20" rx="2" fill="none" stroke="#1565a3" stroke-width="1.3"/><path d="M1 7h26M8 11h12M8 15h9" stroke="#1565a3" stroke-width="1.3"/><path d="M19 14l6 10 1.5-4 4-1z" fill="#fff" stroke="#1565a3" stroke-width="1.2"/></svg>
    <span>BOOK A<br>TOUR</span></div>
  <div class="abs quick" style="left:236px">
    <svg width="22" height="28" viewBox="0 0 22 28"><rect x="1" y="1" width="20" height="26" rx="2" fill="none" stroke="#1565a3" stroke-width="1.3"/><path d="M1 6h20M5 11h12M5 15h12M5 19h8" stroke="#1565a3" stroke-width="1.3"/></svg>
    <span>ENROLMENT<br>APPLICATION<br>FORM</span></div>
  <div class="abs quick" style="left:360px">
    <svg width="28" height="28" viewBox="0 0 28 28"><circle cx="14" cy="9" r="6" fill="none" stroke="#1565a3" stroke-width="1.3"/><path d="M3 18l11 3 11-3v9l-11 0-11 0z" fill="none" stroke="#1565a3" stroke-width="1.3"/><path d="M14 21v6" stroke="#1565a3" stroke-width="1.3"/></svg>
    <span>PROSPECTUS</span></div>
  <div class="abs quick on" style="left:484px">
    <svg width="32" height="30" viewBox="0 0 32 30"><rect x="1" y="9" width="20" height="14" rx="3" fill="none" stroke="#fff" stroke-width="1.3"/><path d="M5 14h12M5 18h9" stroke="#fff" stroke-width="1.3"/><circle cx="23" cy="9" r="8" fill="#1565a3" stroke="#fff" stroke-width="1.3"/><path d="M20.5 7a2.5 2.5 0 1 1 2.5 2.5V11M23 13v1" stroke="#fff" stroke-width="1.3" fill="none"/></svg>
    <span>FAQ</span></div>
</section>

<footer>
  <div class="abs ribbon">
    <h4>INFORMATION RIBBON</h4>
    <p>Lorem Ipsum is simply dummy text of the printing and typesetting industry. Lorem Ipsum has been the industry's standard dummy text ever since the 1500s, when... <u>MORE</u></p>
    <div class="abs stat" style="left:420px;width:120px"><small>CRICOS PROVIDER NUMBER:</small><strong>09981X</strong></div>
    <div class="abs divider"></div>
    <div class="abs stat" style="left:565px;width:90px"><small>ABN:</small><strong>47 210 338 561</strong></div>
  </div>
  <svg class="abs top-btn" width="12" height="14" viewBox="0 0 12 14" aria-label="Back to top"><path d="M6 0 12 14 6 10 0 14z" fill="#fff"/></svg>
  <div class="abs bottom">Brimley College. All rights reserved. &nbsp;|&nbsp; Privacy, Disclaimer &amp; Copyright © 2023</div>
  <div class="abs social foot-social" aria-label="Social links"><span></span><span></span><span></span></div>
</footer>

</body>
</html>
```